Talvor Visit cards serious but not sad

Hello, I'd like to design my visit cards with the logo Talvor (attached) the following information: Name: Karim Belmadi Title: Mobile Director: 33 (0) 6 72 18 35 09 Phone: 33 (0) 4 58 61 07 92 e-mail: karim.belmadi@talvor-consulting.example address: 17 Rue Marcel Danvin 92400 Courbevoie This visit will be used on the banking institutions and Talvor is a consulting firm. I do not want to have dark background.

Target Market(s)

banks

Contact Information for Business Card

Name : Karim Belmadi
Title : Director
mobile : +33(0)6 72 18 35 09
Phone : +33(0)4 58 61 07 92
e-mail: karim.belmadi@talvor-consulting.example
adresse : 17 Rue marcel Danvin 78640 Bellencourt

Requirements
Nice to have
• serious but not sad

```html
<!DOCTYPE html>
<html lang="fr">
<head>
<meta charset="utf-8">
<title>Talvor – cartes de visite</title>
<link rel="stylesheet" href="https://fonts.googleapis.com/css2?family=Roboto:wght@300;400;500&display=swap">
<style>
  :root {
    --bg: #ece9e4;
    --card: #fbfbfb;
    --card-edge: #e3e4e6;
    --brand: #1c9ad6;
    --ink: #6f7378;
    --ink-soft: #8d9196;
  }
  * { margin: 0; padding: 0; box-sizing: border-box; }
  html, body { width: 1200px; height: 1023px; overflow: hidden; }
  body {
    background: var(--bg);
    font-family: "Roboto", sans-serif;
    display: flex;
    flex-direction: column;
    align-items: center;
    justify-content: center;
    gap: 70px;
  }
  .card {
    position: relative;
    width: 700px;
    height: 400px;
    background: linear-gradient(135deg, #ffffff 0%, var(--card) 55%, #eef0f2 100%);
    border-radius: 18px;
    border: 1px solid var(--card-edge);
    box-shadow: 0 10px 28px rgba(60, 50, 40, 0.18);
    overflow: hidden;
  }
  .brand {
    position: absolute;
    display: flex;
    align-items: center;
    gap: 16px;
    color: var(--brand);
    font-weight: 500;
    letter-spacing: 1px;
    line-height: 1;
    white-space: nowrap;
  }
  .brand-dot {
    border-radius: 50%;
    background: var(--brand);
    flex: none;
  }
  .card--front .brand { right: 56px; top: 48px; font-size: 58px; }
  .card--front .brand-dot { width: 72px; height: 72px; }

  .rule {
    position: absolute;
    height: 2px;
    background: var(--brand);
  }
  .card--front .rule { left: 56px; right: 56px; top: 210px; }

  .person { position: absolute; left: 56px; top: 162px; }
  .person-name {
    color: var(--brand);
    font-weight: 400;
    font-size: 38px;
    letter-spacing: 0.5px;
    text-transform: uppercase;
    line-height: 1;
    white-space: nowrap;
  }
  .person-title {
    position: absolute;
    left: 56px; top: 222px;
    color: var(--ink-soft);
    font-size: 17px;
    font-weight: 400;
  }
  .contact {
    position: absolute;
    left: 56px; top: 262px;
    list-style: none;
    color: var(--ink);
    font-size: 17px;
    font-weight: 300;
    line-height: 28px;
    white-space: nowrap;
  }
  .contact li { display: flex; align-items: center; gap: 12px; }
  .contact svg { width: 14px; height: 14px; flex: none; }

  .card--back .brand {
    left: 50%; top: 50%;
    transform: translate(-50%, -60%);
    font-size: 84px;
    gap: 22px;
  }
  .card--back .brand-dot { width: 100px; height: 100px; }
  .card--back .rule { left: 250px; width: 200px; top: 270px; }
</style>
</head>
<body>

<section class="card card--front" aria-label="Recto">
  <div class="brand"><span class="brand-dot"></span><span class="brand-name">Talvor</span></div>
  <div class="person"><h1 class="person-name">Karim Belmadi</h1></div>
  <div class="rule"></div>
  <p class="person-title">Director</p>
  <ul class="contact">
    <li>
      <svg viewBox="0 0 14 14" fill="none" stroke="var(--brand)" stroke-width="1.4"><rect x="3" y="1" width="8" height="12" rx="1.5"/><line x1="6" y1="11" x2="8" y2="11"/></svg>
      +33(0)6 72 18 35 09
    </li>
    <li>
      <svg viewBox="0 0 14 14" fill="var(--brand)"><path d="M3 1.5l2.2 0 1 3-1.4 1.2c.8 1.6 1.9 2.7 3.5 3.5l1.2-1.4 3 1v2.2c0 .6-.5 1-1 1C6.6 12 2 7.4 2 2.5c0-.5.4-1 1-1z"/></svg>
      +33(0)4 58 61 07 92
    </li>
    <li>
      <svg viewBox="0 0 14 14" fill="none" stroke="var(--brand)" stroke-width="1.4"><rect x="1" y="3" width="12" height="9" rx="1"/><polyline points="1.5,3.5 7,8 12.5,3.5"/></svg>
      karim.belmadi@talvor-consulting.example
    </li>
    <li>
      <svg viewBox="0 0 14 14" fill="var(--brand)"><path d="M7 1a4.2 4.2 0 0 0-4.2 4.2C2.8 8.4 7 13 7 13s4.2-4.6 4.2-7.8A4.2 4.2 0 0 0 7 1zm0 5.8a1.6 1.6 0 1 1 0-3.2 1.6 1.6 0 0 1 0 3.2z"/></svg>
      17 Rue marcel Danvin 78640 Bellencourt
    </li>
  </ul>
</section>

<section class="card card--back" aria-label="Verso">
  <div class="brand"><span class="brand-dot"></span><span class="brand-name">Talvor</span></div>
  <div class="rule"></div>
</section>

</body>
</html>
```